The Shelf Sage needs a pricing flyer

Single page flyer for the Shelf Sage.
The Shelf Sage is a lead generation service exclusively for the custom closet industry.
You design quality closets we provide quality leads!
Value Points:
Leads for closet companies are exclusive with a first right of refusal. Meaning, if the closet company cannot handle all of the leads we can provide, we will sell the excess to other closet companies. We will never sell the same lead to two different closet companies.
Benefits:
Flat rate and easy to budget
Cancel at anytime
Choose from 3 types of leads
Lower cost compared to overall cost per lead from other sources
More leads allows hiring more designers
More leads grow the companies revenue
Less time managing other advertising models
3 service options.
$250 each
- We send you the lead
- You and your team set the appointment
- Setting the appointment is up to you
2. $275 each
- We send you the lead
- We guarantee the appointment
- Return unset appointments for a replacement
3. $375 each
- We are your call center
- We generate the lead
- We set the appointment
Contact:
The Shelf Sage
704-555-0183
leads@TheShelfSage.example

```html
<!DOCTYPE html>
<html lang="en">
<head>
<meta charset="utf-8">
<title>The Shelf Sage – Pricing Flyer</title>
<link rel="stylesheet" href="https://fonts.googleapis.com/css2?family=Cinzel:wght@400;700&family=Marcellus&family=Great+Vibes&family=Oswald:wght@500&family=Lato:wght@400;700&display=swap">
<style>
  :root {
    --stage: #000000;
    --paper: #ffffff;
    --brown: #a9662f;
    --brown-dark: #8c5223;
    --beige: #f3ebe4;
    --beige-deep: #ead9c9;
    --ink: #333333;
    --ink-soft: #555555;
    --photo-sketch: #e4e0db;
    --photo-dark: #4a3428;
    --photo-white: #e9e6e1;
    --photo-navy: #3c4150;
  }
  * { margin: 0; padding: 0; box-sizing: border-box; }
  html, body { width: 1200px; height: 1200px; overflow: hidden; background: var(--stage); }
  .flyer {
    position: absolute; left: 220px; top: 66px; width: 756px; height: 1068px;
    background: var(--paper); overflow: hidden;
    font-family: "Lato", sans-serif; color: var(--ink);
  }
  .hero-panel {
    position: absolute; left: 0; top: 0; width: 756px; height: 292px;
    background: linear-gradient(90deg, #f7f1ec, var(--beige));
  }
  .hero-image {
    position: absolute; left: 0; top: 0; width: 480px; height: 292px;
    background: linear-gradient(100deg, var(--photo-sketch) 0%, #f1eeea 60%, #d9c8b5 100%);
    clip-path: polygon(0 0, 100% 0, 91% 100%, 0 100%);
  }
  .hero-edge {
    position: absolute; left: 470px; top: 0; width: 40px; height: 292px;
    background: var(--beige-deep);
    clip-path: polygon(10px 0, 40px 0, 0 292px, -20px 292px);
    opacity: .7;
  }
  .brand {
    position: absolute; left: 478px; top: 58px; width: 260px; text-align: center;
    font-family: "Marcellus", serif; font-size: 30px; line-height: 34px; color: var(--brown-dark);
  }
  .brand-mark {
    display: block; width: 14px; height: 14px; border-radius: 50%;
    background: var(--brown); margin: 0 auto 10px;
  }
  .headline {
    position: absolute; left: 478px; top: 138px; width: 260px; text-align: center;
    font-family: "Cinzel", serif; font-size: 25px; line-height: 32px;
  }
  .headline .light { color: var(--brown); font-weight: 400; }
  .headline .strong { color: var(--ink-soft); font-weight: 700; }
  .tagline-band {
    position: absolute; left: 0; top: 300px; width: 756px; height: 36px;
    background: var(--brown); color: var(--paper);
    font-family: "Marcellus", serif; font-size: 17.5px; line-height: 36px;
    text-align: center; letter-spacing: .3px;
  }
  .gallery {
    position: absolute; left: 25px; top: 353px; width: 333px; height: 655px;
    border: 2px solid var(--brown);
  }
  .gallery-photo { position: absolute; left: 11px; width: 309px; }
  .photo-walkin { top: 11px; height: 202px; background: linear-gradient(160deg, var(--photo-dark), #7a5c48 55%, #d8d3cc); }
  .photo-white { top: 222px; height: 205px; background: linear-gradient(160deg, #cfcac3, var(--photo-white) 60%, #d3ccc4); }
  .photo-office { top: 437px; height: 204px; background: linear-gradient(170deg, #f0eeea, var(--photo-navy) 55%, #8b6b52); }
  .intro {
    position: absolute; left: 388px; top: 360px; width: 342px;
    font-size: 13.2px; line-height: 17.4px; text-align: justify; color: var(--ink);
  }
  .options-title {
    position: absolute; left: 388px; top: 472px;
    font-family: "Great Vibes", cursive; font-weight: 400; font-size: 38px; line-height: 44px; color: var(--brown);
  }
  .plan { position: absolute; left: 385px; width: 345px; }
  .plan-price {
    position: absolute; left: 0; top: 0; bottom: 0; width: 107px;
    background: var(--beige); border: 1.5px solid var(--brown); border-radius: 10px;
    display: flex; flex-direction: column; align-items: center; justify-content: center;
  }
  .amount { font-family: "Oswald", sans-serif; font-weight: 500; font-size: 40px; line-height: 42px; color: var(--brown); }
  .per { font-size: 14px; color: var(--ink); line-height: 16px; }
  .plan-details {
    position: absolute; left: 111px; right: 0; top: 0; bottom: 0;
    border: 1.5px solid var(--brown); border-radius: 10px;
    display: flex; align-items: center; padding-left: 12px;
  }
  .plan-details ul { list-style: none; font-size: 13.5px; line-height: 16.8px; }
  .plan-details li { position: relative; padding-left: 13px; }
  .plan-details li::before {
    content: ""; position: absolute; left: 2px; top: 6px; width: 5px; height: 5px;
    border-radius: 50%; background: var(--brown);
  }
  .plan-basic { top: 522px; height: 98px; }
  .plan-guaranteed { top: 629px; height: 127px; }
  .plan-callcenter { top: 763px; height: 74px; }
  .benefits-panel {
    position: absolute; left: 440px; top: 901px; width: 316px; height: 167px;
    background: var(--beige);
    clip-path: polygon(14% 0, 100% 0, 100% 100%, 0 100%);
  }
  .benefits-band {
    position: absolute; left: 498px; top: 871px; width: 258px; height: 30px;
    background: var(--brown); color: var(--paper);
    font-family: "Marcellus", serif; font-size: 15px; letter-spacing: 4px;
    display: flex; align-items: center; justify-content: center; gap: 8px;
  }
  .benefits-band .rule { width: 34px; height: 1px; background: var(--paper); }
  .benefits-list {
    position: absolute; left: 456px; top: 918px; width: 296px;
    list-style: none; text-align: center; font-size: 13.2px; line-height: 16.8px; color: var(--ink);
  }
  .benefits-list li::before { content: "• "; color: var(--brown); }
  .contact-band {
    position: absolute; left: 17px; top: 1026px; width: 424px; height: 30px;
    background: var(--brown); color: var(--paper);
    font-size: 14px; line-height: 30px; padding-left: 20px;
    clip-path: polygon(0 0, 100% 0, 97% 100%, 0 100%);
  }
</style>
</head>
<body>
<main class="flyer">
  <section class="hero">
    <div class="hero-panel"></div>
    <div class="hero-image" role="img" aria-label="Pencil sketch of a walk-in closet with a hand drawing the shelves"></div>
    <div class="hero-edge"></div>
    <div class="brand"><span class="brand-mark"></span>The Shelf Sage</div>
    <h1 class="headline">
      <span class="light">YOU DESIGN</span><br>
      <span class="strong">QUALITY CLOSETS</span><br>
      <span class="light">WE PROVIDE</span><br>
      <span class="strong">QUALITY LEADS!</span>
    </h1>
  </section>

  <div class="tagline-band">A LEAD GENERATION SERVICE EXCLUSIVELY FOR THE CUSTOM CLOSET INDUSTRY.</div>

  <div class="gallery">
    <div class="gallery-photo photo-walkin" role="img" aria-label="Dark wood walk-in closet with a center island"></div>
    <div class="gallery-photo photo-white" role="img" aria-label="White closet with hanging clothes and shoe shelves"></div>
    <div class="gallery-photo photo-office" role="img" aria-label="Navy built-in cabinets in a home office"></div>
  </div>

  <p class="intro">Leads for closet companies are exclusive with a first right of refusal. Meaning, if the closet company cannot handle all of the leads we can provide, we will sell the excess to other closet companies. We will never sell the same lead to two different closet companies.</p>

  <h2 class="options-title">3 Service Options</h2>

  <div class="plan plan-basic">
    <div class="plan-price"><span class="amount">$250</span><span class="per">each</span></div>
    <div class="plan-details"><ul>
      <li>We send you the lead</li>
      <li>You and your team set<br>&nbsp;the appointment</li>
      <li>Setting the appointment<br>is up to you</li>
    </ul></div>
  </div>

  <div class="plan plan-guaranteed">
    <div class="plan-price"><span class="amount">$275</span><span class="per">each</span></div>
    <div class="plan-details"><ul>
      <li>We send you the lead</li>
      <li>You and your team set<br>&nbsp;the appointment</li>
      <li>We guarantee the appointment</li>
      <li>Return unset appointments<br>for a replacement</li>
    </ul></div>
  </div>

  <div class="plan plan-callcenter">
    <div class="plan-price"><span class="amount">$375</span><span class="per">each</span></div>
    <div class="plan-details"><ul>
      <li>We are your call center</li>
      <li>We generate the lead</li>
      <li>We set the appointment</li>
    </ul></div>
  </div>

  <div class="benefits-panel"></div>
  <div class="benefits-band"><span class="rule"></span>BENEFITS<span class="rule"></span></div>
  <ul class="benefits-list">
    <li>Flat rate and easy to budget</li>
    <li>Cancel at anytime</li>
    <li>Choose from 3 types of leads</li>
    <li>Lower cost compared to overall cost<br>per lead from other sources</li>
    <li>More leads allows hiring more designers</li>
    <li>More leads grow the companies revenue</li>
    <li>Less time managing other advertising models</li>
  </ul>

  <div class="contact-band">The Shelf Sage | 704-555-0183 | leads@TheShelfSage.example</div>
</main>
</body>
</html>
```